Urine collection cup with and without sterile seal sticker

Hello. We need a urine cup label designed please with

Name:
Date of Birth:
Date:
Time:
Temp℃:
Specimen ID:

Product code: TUB-47
Volume markings (e.g., 30 mL, 60 mL, 90 mL).
Vela Drug Tests logo

Could you please provide one version with the additional sterile sticker extending to the top, and one version without the additional sterile sticker?

```html
<!DOCTYPE html>
<html lang="en">
<head>
<meta charset="utf-8">
<title>Vela Drug Tests – TUB-47 Urine Cup Labels</title>
<link rel="stylesheet" href="https://fonts.googleapis.com/css2?family=Barlow+Semi+Condensed:wght@500;600&family=Barlow:wght@700&display=swap">
<style>
  :root {
    --brand-blue: #0e98cf;
    --panel-navy: #314051;
    --paper: #ffffff;
  }
  html, body {
    margin: 0;
    padding: 0;
    width: 1200px;
    height: 800px;
    overflow: hidden;
    background: var(--paper);
  }
  .label-sheet {
    display: block;
    width: 1200px;
    height: 800px;
  }
  .label-frame { fill: var(--brand-blue); }
  .write-area { fill: var(--paper); }
  .panel-gap { fill: var(--paper); }
  .code-panel { fill: var(--panel-navy); }
  .field-rule { stroke: var(--brand-blue); stroke-width: 4; }
  .volume-box { fill: none; stroke: var(--brand-blue); stroke-width: 4; }
  .field-label {
    fill: var(--brand-blue);
    font-family: "Barlow Semi Condensed", sans-serif;
    font-weight: 600;
    font-size: 50px;
  }
  .volume-label {
    fill: var(--brand-blue);
    font-family: "Barlow Semi Condensed", sans-serif;
    font-weight: 500;
    font-size: 43px;
  }
  .sterile-word {
    fill: var(--paper);
    font-family: "Barlow", sans-serif;
    font-weight: 700;
    font-size: 100px;
  }
  .product-code {
    fill: var(--paper);
    font-family: "Barlow", sans-serif;
    font-weight: 700;
    font-size: 70px;
  }
  .brand-name {
    fill: var(--paper);
    font-family: "Barlow Semi Condensed", sans-serif;
    font-weight: 600;
    font-size: 34px;
    letter-spacing: 2px;
  }
</style>
</head>
<body>
<svg class="label-sheet" viewBox="0 0 2250 1500" xmlns="http://www.w3.org/2000/svg" aria-label="Vela Drug Tests TUB-47 urine cup labels, with and without sterile seal">
  <defs>
    <g id="label-body">
      <rect class="label-frame" x="162" y="586" width="896" height="710" rx="55"/>
      <path class="write-area" d="M248 641 H830 V1240 H248 A30 30 0 0 1 218 1210 V671 A30 30 0 0 1 248 641 Z"/>

      <g class="fields">
        <text class="field-label" x="246" y="720">Date of Birth:</text>
        <line class="field-rule" x1="248" y1="746" x2="830" y2="746"/>
        <text class="field-label" x="246" y="812">Date:</text>
        <line class="field-rule" x1="248" y1="838" x2="830" y2="838"/>
        <text class="field-label" x="246" y="904">Time:</text>
        <line class="field-rule" x1="248" y1="930" x2="830" y2="930"/>
        <text class="field-label" x="246" y="996">Temp°C:</text>
        <line class="field-rule" x1="248" y1="1022" x2="830" y2="1022"/>
        <text class="field-label" x="246" y="1088">Specimen ID:</text>
        <line class="field-rule" x1="248" y1="1113" x2="830" y2="1113"/>
      </g>

      <g class="volumes">
        <rect class="volume-box" x="251" y="1156" width="38" height="38"/>
        <text class="volume-label" x="304" y="1191">30 mL</text>
        <rect class="volume-box" x="445" y="1156" width="38" height="38"/>
        <text class="volume-label" x="498" y="1191">60 mL</text>
        <rect class="volume-box" x="639" y="1156" width="38" height="38"/>
        <text class="volume-label" x="692" y="1191">90 mL</text>
      </g>

      <path class="panel-gap" d="M872 1296 V858 A80 80 0 0 1 952 778 H1058 V1296 Z"/>
      <path class="code-panel" d="M883 1296 V860 A70 70 0 0 1 953 790 H1058 V1241 A55 55 0 0 1 1003 1296 Z"/>
      <text class="product-code" transform="translate(915 915) rotate(90)" textLength="255" lengthAdjust="spacingAndGlyphs">TUB-47</text>
      <text class="brand-name" transform="translate(992 918) rotate(90)">VELA DRUG TESTS</text>
    </g>
  </defs>

  <g class="label label--sterile">
    <path class="label-frame sterile-tab" d="M830 800 V259 A55 55 0 0 1 885 204 H1003 A55 55 0 0 1 1058 259 V800 Z"/>
    <use href="#label-body"/>
    <text class="sterile-word" transform="translate(915 290) rotate(90)" textLength="432" lengthAdjust="spacing">STERILE</text>
  </g>

  <g class="label label--plain" transform="translate(1030 0)">
    <use href="#label-body"/>
  </g>
</svg>
</body>
</html>
```